Modern and Clean Web Re-Design Project

We have 2 companies in similar industries: Printing and Mail Preparation/Fulfillment. We prefer sites that are clean and easy to navigate.Our printing company, Harbourline Press Works' website, hpwdirect.example is outdated needs revamping. We have rebranded our logo and are looking for a new design that is clean, modern and geared to other corporations and business in the downtown Toronto area. Our mailing company, The Postwick Depot (thepostwickdepot.example) needs a website as well. This company is in the Direct Mail and letter shop business, which essentially is addressing/personalizing people's printed matter and preparing it for either the Canadian or US postal service. The Postwick Depot specializes in not-for-profit and corporate sectors.Please see our logos to get an idea of the colors and look we want. For all intensive purposes, the sites can look similar in design all we want is that each site has the appropriate corporate colors and is a bit different so they don't look identical as the two business run as separate corporations.The content of the website should be easily changed by our staff and we want it to be setup to optimized for SEO based on the keywords we want. We are looking for someone to work on this project immediately
Updates

Project Deadline Extended
Reason: Change of ideas

After doing some thinking, I would like the site to be more modern but the non flash sites that I have seen so far Im finding life-less and while I want something clean, not overly busy and corporate looking, I dont want the design to be bland looking.

Please design with the previous specs in mind but with a twist as mentioned above.

Thanks
Dorian

Target Market(s)

See above

Industry/Entity Type

Printing

Requirements
Must have
• Must match the design and style of each respective logoSee the attached impage of the front of our offices to have an idea of our lookWe must be able to edit the content ourselves without any fancy programs or tools.Must be SEO optimized
Nice to have
• An online order form that can be emailed to us for quotes.....perhaps a page with a bunch of fields that have drop down menus....
Should not have
• Should not be overly busy. I want it to be clean and simple but informative without being hard to navigate

```html
<!DOCTYPE html>
<html lang="en">
<head>
<meta charset="utf-8">
<title>Harbourline Press Works — Digital Printing</title>
<link rel="stylesheet" href="https://fonts.googleapis.com/css2?family=Sanchez&family=Russo+One&family=Share+Tech+Mono&family=Roboto:wght@400;700&display=swap">
<style>
  :root {
    --navy: #0b2d55;
    --orange: #f5a91c;
    --page: #fbfbfb;
    --white: #ffffff;
    --ink: #1a1a1a;
    --icon: #4a4a4a;
    --map: #d9d6cf;
  }
  * { box-sizing: border-box; margin: 0; padding: 0; }
  html, body { width: 1200px; height: 996px; overflow: hidden; }
  body {
    position: relative;
    background: var(--page);
    font-family: "Sanchez", Georgia, serif;
    color: var(--navy);
  }
  .top-rule { position: absolute; left: 0; top: 0; width: 1200px; height: 8px; background: var(--navy); }

  /* header */
  .brand {
    position: absolute; left: 120px; top: 30px;
    display: flex; align-items: center; gap: 10px;
    font-family: "Sanchez", Georgia, serif; font-size: 22px; color: var(--navy);
    line-height: 1.05; width: 190px;
  }
  .brand-mark { width: 16px; height: 16px; background: var(--orange); flex: none; }
  .contact {
    position: absolute; right: 188px; top: 22px;
    display: flex; align-items: center; gap: 8px;
    font-family: "Roboto", Arial, sans-serif; font-size: 14px; color: var(--ink);
  }
  .contact svg { display: block; }
  .contact .sep { margin: 0 6px; }
  .social { position: absolute; left: 1030px; top: 20px; display: flex; gap: 6px; }
  .social span { width: 20px; height: 20px; border-radius: 50%; background: var(--navy); }
  .main-nav {
    position: absolute; left: 575px; top: 56px; display: flex;
    font-size: 15.5px; color: var(--navy);
  }
  .main-nav a { display: block; height: 38px; padding: 2px 0 0; text-align: center; color: inherit; text-decoration: none; }
  .main-nav a:nth-child(1) { width: 132px; border-bottom: 7px solid var(--navy); }
  .main-nav a:nth-child(2) { width: 150px; }
  .main-nav a:nth-child(3) { width: 100px; }
  .main-nav a:nth-child(4) { width: 130px; }

  /* hero */
  .hero-band { position: absolute; left: 0; top: 94px; width: 1200px; height: 234px; background: var(--orange); }
  .hero {
    position: absolute; left: 120px; top: 112px; width: 960px; height: 329px;
    background: var(--white); overflow: hidden;
  }
  .hero-visual {
    position: absolute; left: 0; top: 0; width: 960px; height: 329px;
    background:
      linear-gradient(180deg, rgba(255,255,255,0) 62%, rgba(255,255,255,0) 100%),
      linear-gradient(90deg, #3c3c3e 0%, #5a5a5e 6%, #b04d8a 30%, #d27ab0 46%, #5e5e62 62%, rgba(255,255,255,0) 66%),
      linear-gradient(90deg, #ffffff 0%, #ffffff 100%);
  }
  .hero-visual::after {
    content: ""; position: absolute; left: 0; bottom: 0; width: 960px; height: 110px;
    background: linear-gradient(90deg, #3f9a2e 0%, #e63a1e 22%, #1e6fb8 40%, #1aa39a 55%, #8fbf24 70%, #e5241f 82%, #f0c420 100%);
    opacity: .85;
  }
  .hero-title {
    position: absolute; left: 678px; top: 82px; color: #111;
    text-align: center; line-height: 1;
  }
  .hero-title .big { display: block; font-family: "Russo One", Arial, sans-serif; font-size: 53px; letter-spacing: 2px; }
  .hero-title .small { display: block; margin-top: 10px; font-family: "Share Tech Mono", monospace; font-size: 36px; letter-spacing: 8px; }

  /* steps */
  .step {
    position: absolute; top: 479px; width: 244px; height: 244px; border-radius: 50%;
    background: var(--orange); text-align: center;
  }
  .step-1 { left: 121px; }
  .step-2 { left: 477px; }
  .step-3 { left: 833px; }
  .step-num {
    position: absolute; left: 0; top: 1px; width: 56px; height: 56px; border-radius: 50%;
    background: var(--navy); color: var(--white); font-size: 30px; line-height: 56px;
  }
  .step-icon { position: absolute; left: 82px; top: 55px; }
  .step-label { position: absolute; left: 0; right: 0; top: 160px; font-size: 22px; line-height: 26px; color: var(--navy); }
  .flow-arrow { position: absolute; top: 550px; }
  .flow-arrow.a1 { left: 375px; }
  .flow-arrow.a2 { left: 731px; }

  /* footer */
  .site-footer { position: absolute; left: 0; top: 759px; width: 1200px; height: 228px; background: var(--navy); color: var(--white); }
  .bottom-rule { position: absolute; left: 0; top: 987px; width: 1200px; height: 9px; background: var(--orange); }
  .about { position: absolute; left: 120px; top: 26px; width: 320px; }
  .about h2 { font-weight: 400; font-size: 17px; letter-spacing: .5px; margin-bottom: 18px; }
  .about p { font-size: 12.2px; line-height: 18.75px; }
  .map {
    position: absolute; left: 486px; top: 29px; width: 295px; height: 162px;
    background: linear-gradient(160deg, #ecebe6 0%, var(--map) 55%, #c9c6be 100%);
    border: 2px solid var(--white);
  }
  .footer-brand {
    position: absolute; left: 850px; top: 36px; width: 230px;
    display: flex; align-items: center; gap: 10px; justify-content: flex-end;
    font-size: 30px; line-height: 1.05; text-align: right;
  }
  .footer-brand .brand-mark { width: 20px; height: 20px; }
  .copyright {
    position: absolute; right: 130px; top: 150px; text-align: right;
    font-family: "Roboto", Arial, sans-serif; font-size: 12.5px; line-height: 19px;
  }
</style>
</head>
<body>
  <div class="top-rule"></div>

  <header class="site-header">
    <div class="brand"><span class="brand-mark"></span><span>Harbourline Press Works</span></div>
    <div class="contact">
      <svg width="18" height="13" viewBox="0 0 18 13" aria-hidden="true"><path d="M1 5 L9 1 L17 5 V12 H1 Z M1 5 L9 9 L17 5" fill="none" stroke="#1a1a1a" stroke-width="1.6"/></svg>
      <span>info@hpwdirect.example</span>
      <span class="sep">|</span>
      <svg width="18" height="16" viewBox="0 0 18 16" aria-hidden="true"><path d="M3 2 C1 4 3 9 7 12 C11 15 14 15 16 13 L13 10 L11 11 C9 10 7 8 6 6 L7 4 Z" fill="#1a1a1a"/></svg>
      <span>416-555-0147</span>
    </div>
    <div class="social" aria-label="Social links"><span></span><span></span></div>
    <nav class="main-nav">
      <a href="#">Who are we</a>
      <a href="#">What do we do</a>
      <a href="#">Email a file</a>
      <a href="#">Contact us</a>
    </nav>
  </header>

  <div class="hero-band"></div>
  <section class="hero">
    <div class="hero-visual" role="img" aria-label="Wide-format digital printer printing a pink orchid photo over a band of colourful pixel squares"></div>
    <h1 class="hero-title"><span class="big">DIGITAL</span><span class="small">PRINTING</span></h1>
  </section>

  <section class="steps">
    <div class="step step-1">
      <div class="step-num">1</div>
      <svg class="step-icon" width="80" height="92" viewBox="0 0 80 92" aria-hidden="true">
        <rect x="4" y="10" width="72" height="80" rx="2" fill="#fff" stroke="#4a4a4a" stroke-width="4"/>
        <rect x="22" y="4" width="36" height="12" rx="3" fill="#fff" stroke="#4a4a4a" stroke-width="4"/>
        <circle cx="40" cy="6" r="4" fill="#4a4a4a"/>
      </svg>
      <div class="step-label">order &amp;<br>send file</div>
    </div>
    <svg class="flow-arrow a1" width="96" height="60" viewBox="0 0 96 60" aria-hidden="true">
      <path d="M3 20 L62 18 L60 3 L93 30 L60 57 L61 42 L3 42 Z" fill="#fff" stroke="#333" stroke-width="3" stroke-linejoin="round"/>
    </svg>
    <div class="step step-2">
      <div class="step-num">2</div>
      <svg class="step-icon" width="92" height="84" viewBox="0 0 92 84" aria-hidden="true" style="left:76px">
        <rect x="3" y="3" width="86" height="76" rx="16" fill="#fff" stroke="#4a4a4a" stroke-width="5"/>
        <path d="M10 68 L34 36 L46 50 L62 26 L80 68 Z" fill="#4a4a4a"/>
      </svg>
      <div class="step-label">print</div>
    </div>
    <svg class="flow-arrow a2" width="96" height="60" viewBox="0 0 96 60" aria-hidden="true">
      <path d="M3 20 L62 18 L60 3 L93 30 L60 57 L61 42 L3 42 Z" fill="#fff" stroke="#333" stroke-width="3" stroke-linejoin="round"/>
    </svg>
    <div class="step step-3">
      <div class="step-num">3</div>
      <svg class="step-icon" width="84" height="92" viewBox="0 0 84 92" aria-hidden="true" style="left:80px">
        <rect x="4" y="3" width="76" height="72" rx="14" fill="#fff" stroke="#4a4a4a" stroke-width="5"/>
        <line x1="42" y1="3" x2="42" y2="75" stroke="#4a4a4a" stroke-width="5"/>
        <line x1="4" y1="39" x2="80" y2="39" stroke="#4a4a4a" stroke-width="5"/>
        <circle cx="16" cy="83" r="6" fill="#fff" stroke="#4a4a4a" stroke-width="4"/>
        <circle cx="68" cy="83" r="6" fill="#fff" stroke="#4a4a4a" stroke-width="4"/>
      </svg>
      <div class="step-label">delivery</div>
    </div>
  </section>

  <footer class="site-footer">
    <div class="about">
      <h2>ABOUT HPW</h2>
      <p>We maintain absolute integrity in every aspect of our operation. By using our experience to understand our customers' expectations, we show an uncommon commitment to achieving a high-quality product under strict deadlines. It is the customers who set the standards we strive to achieve. We are professionals who bring unique and specialized skills you can depend on.</p>
    </div>
    <div class="map" role="img" aria-label="Street map showing the shop location"></div>
    <div class="footer-brand"><span class="brand-mark"></span><span>Harbourline Press Works</span></div>
    <div class="copyright">copyright (c) HPW Direct 2013<br>all rights reserved</div>
  </footer>
  <div class="bottom-rule"></div>
</body>
</html>
```